Tallbrook Meridian Advisory needs business cards

Tallbrook Meridian Advisory is a new approach to consulting: we believe in partnering our clients in a hands-on, side-by-side, rolling-up-our sleeves approach, rather than being removed and aloof consultants.

We have a logo design developped through PixelHarbor (see attachment) and need to move to the stage of designing a business card for our 7 founding members.

Target Market(s)

Senior executives in local and global companies (such as Fizzmont Tonic, Hollanby, Brevard, etc)

Industry/Entity Type

Business

Requirements
Must have
• Look and feel: The design reflect the logo: i.e. professional, modern and approachable (as opposed to corporate traditional and remote). We are looking for a high quality, premium design.

Content must haves:
- prominent: our logo, person's name, function, phone number and e-mail address
- less prominent: company address and website

Example: Tallbrook Meridian Advisory logo, Mireille Vostag, Partner, +44 (0)781 209 3375, mireille_vostag@tallbrookmeridian.example / 17 Pelham Crescent, Wrensford, Halvershire, UK, HV4 3WN - www.tallbrookmeridian.example

- Both sides of the card can be used
- Both versions of the logo can be used (on black or on white)

```html
<!DOCTYPE html>
<html lang="en">
<head>
<meta charset="utf-8">
<title>Tallbrook Meridian Advisory – Business Card</title>
<link href="https://fonts.googleapis.com/css2?family=Arimo:wght@400;700&display=swap" rel="stylesheet">
<style>
  :root {
    --page: #ffffff;
    --card: #e6e6e6;
    --ink: #6f6d7d;
    --ink-dark: #222222;
    --brand-blue: #1c9fe0;
    --shadow: rgba(0, 0, 0, 0.35);
  }
  html, body {
    margin: 0;
    padding: 0;
    width: 1200px;
    height: 750px;
    overflow: hidden;
    background: var(--page);
    font-family: "Arimo", Arial, sans-serif;
  }
  .stage { position: relative; width: 1200px; height: 750px; }
  .card {
    position: absolute;
    top: 262px;
    width: 407px;
    height: 226px;
    background: var(--card);
    border-radius: 8px;
    box-shadow: 0 1px 4px var(--shadow);
  }
  .card--front { left: 124px; }
  .card--back { left: 668px; color: var(--ink); }

  /* Front */
  .brand-lockup {
    position: absolute;
    left: 89px;
    top: 69px;
    display: flex;
    align-items: center;
    gap: 11px;
  }
  .brand-lockup__dot {
    width: 82px;
    height: 82px;
    border-radius: 50%;
    background: var(--brand-blue);
  }
  .brand-lockup__name {
    color: var(--ink-dark);
    font-size: 20px;
    font-weight: 400;
    line-height: 1.1;
    letter-spacing: -0.3px;
  }

  /* Back */
  .holder { position: absolute; left: 24px; top: 21px; }
  .holder__name { font-size: 23px; font-weight: 700; line-height: 1; margin: 0; }
  .holder__role { font-size: 17px; font-weight: 400; line-height: 1; margin: 3px 0 0; }

  .brand-mark {
    position: absolute;
    right: 21px;
    top: 23px;
    text-align: right;
    font-size: 12px;
    font-weight: 400;
    line-height: 1.15;
    color: var(--ink);
  }

  .contacts { position: absolute; left: 24px; top: 106px; list-style: none; margin: 0; padding: 0; }
  .contacts__item { display: flex; align-items: center; gap: 4px; font-size: 11px; height: 17px; }
  .contacts__badge {
    width: 11px; height: 11px; border-radius: 50%;
    background: var(--ink); color: var(--card);
    font-size: 8px; font-weight: 700;
    display: inline-flex; align-items: center; justify-content: center;
  }

  .address {
    position: absolute; left: 23px; top: 188px;
    font-size: 7px; line-height: 1.35; font-style: normal;
  }
  .website {
    position: absolute; right: 20px; top: 196px;
    font-size: 7.5px;
  }
</style>
</head>
<body>
<main class="stage">
  <section class="card card--front" aria-label="Card front">
    <div class="brand-lockup">
      <span class="brand-lockup__dot" aria-hidden="true"></span>
      <span class="brand-lockup__name">Tallbrook Meridian<br>Advisory</span>
    </div>
  </section>

  <section class="card card--back" aria-label="Card back">
    <div class="holder">
      <h1 class="holder__name">Mireille Vostag</h1>
      <p class="holder__role">Partner</p>
    </div>
    <div class="brand-mark">Tallbrook Meridian<br>Advisory</div>
    <ul class="contacts">
      <li class="contacts__item"><span class="contacts__badge">P</span>+44 (0)781 209 3375</li>
      <li class="contacts__item"><span class="contacts__badge">E</span>mireille_vostag@tallbrookmeridian.example</li>
    </ul>
    <address class="address">17 Pelham Crescent<br>Wrensford, Halvershire, UK, HV4 3WN</address>
    <div class="website">www.tallbrookmeridian.example</div>
  </section>
</main>
</body>
</html>
```